Flyer FMLP

Everyone deserves true happiness.
Real Food is the answer to:
A body you love
Reverting illnesses
Healthy digestion
Stable blood sugar
Emotions in control
Blasting energy
Sound sleep
REAL food + water + exercise + Laughter =
“HIGH QUALITY OF LIFE “
EASY, right?
Challenging: certainly
Changing habits: reluctance in sight!
WE’RE OFFER TO:
1. Study YOUR unique body composition, food cravings, blockages, illnesses, and personality!
2. Introduce you to new Food
3. customized wellness plan with follow ups
4. meditation,cooking, and fitness classes as well as wellness workshops
5. New friends with high aspirations
LOGO
Contact info
Please visit our web address to see our design style and colors: www.freshmeadowlifepath.net
Target Market(s)
people who want to be more healthy
Industry/Entity Type
Fitness
Requirements
Must have
- beautiful pictures of fresh food (main picture) and maybe a few more small pictures reflecting
exercise
healthy living
meditation
Nice to have
- look is crucial. recall some of the color or colors from my logo to have a theme

```html
<!DOCTYPE html>
<html lang="en">
<head>
<meta charset="utf-8">
<title>FMLP Flyer</title>
<link rel="stylesheet" href="https://fonts.googleapis.com/css2?family=Philosopher:wght@400;700&family=Libre+Baskerville:wght@700&family=Great+Vibes&display=swap">
<style>
  :root{
    --leaf:#8cb512;
    --leaf-dark:#6f9410;
    --leaf-ring:#9ec22c;
    --leaf-pale:#eef3d8;
    --leaf-soft:#d7e6a3;
    --sun:#f2c21a;
    --amber:#e9a21a;
    --forest:#1f6b2a;
    --ember:#e8552a;
    --ink:#1d1d1d;
    --paper:#ffffff;
    --backdrop:#e4e4e4;
    --text-font:"Philosopher", sans-serif;
    --url-font:"Libre Baskerville", serif;
    --script-font:"Great Vibes", cursive;
  }
  *{box-sizing:border-box;margin:0;padding:0}
  html,body{width:1200px;height:900px;overflow:hidden}
  body{background:var(--backdrop);position:relative;font-family:var(--text-font);color:var(--ink)}
  .card{position:absolute;top:51px;width:357px;height:795px;background:var(--paper);border:1px solid #333;overflow:hidden}
  .card--info{left:187px}
  .card--cover{left:677px}
  .abs{position:absolute}
  .center{left:0;right:0;text-align:center}

  /* info card */
  .info-bg{position:absolute;left:0;top:0}
  .benefits-title{top:26px;color:var(--paper);font-size:22px;font-weight:700}
  .benefit{position:absolute;font-size:16px;font-weight:700;white-space:nowrap}
  .benefit--sun{color:var(--sun)}
  .benefit--forest{color:var(--forest)}
  .benefit--ember{color:var(--ember)}
  .equation{top:296px;font-size:14.5px}
  .equation .plus{color:var(--sun);font-size:26px;font-weight:700;vertical-align:-4px;margin:0 4px}
  .result{top:326px;font-size:14.5px;font-weight:700}
  .result .equals{color:var(--sun);font-size:26px;vertical-align:-4px;margin-right:6px}
  .easy{top:388px;font-size:23px;font-weight:700;color:var(--amber)}
  .challenge{top:424px;font-size:13.5px;line-height:18px}
  .offer-title{top:474px;font-size:23px;font-weight:700;color:var(--amber)}
  .step{position:absolute;display:flex;align-items:flex-start;gap:7px;font-size:11.5px;line-height:14px}
  .step-num{flex:0 0 26px;height:26px;border-radius:50%;background:var(--leaf);color:var(--paper);font-weight:700;font-style:italic;font-size:18px;line-height:26px;text-align:center}
  .footer{position:absolute;left:0;right:0;bottom:0;height:26px;text-align:center;font-family:var(--url-font);font-size:11.5px;line-height:26px}
  .footer--leaf{background:var(--leaf);color:var(--paper)}
  .footer--soft{background:var(--leaf-soft);color:var(--ink)}

  /* cover card */
  .food-photo{top:0;left:0;width:357px;height:210px;background:radial-gradient(circle at 18% 35%,#d7321c 0 16%,transparent 30%),radial-gradient(circle at 75% 30%,#f2d21a 0 18%,transparent 34%),linear-gradient(180deg,#7fb43a 0%,#4f8a26 55%,#ffffff 100%)}
  .brand{top:250px;left:16px;display:flex;align-items:center;gap:10px}
  .brand-dot{width:60px;height:60px;border-radius:50%;background:var(--leaf)}
  .brand-name{font-size:24px;font-weight:700;color:var(--leaf-dark)}
  .brand-tag{top:302px;left:88px;font-size:7.5px;letter-spacing:.6px;color:var(--ink);white-space:nowrap}
  .cover-bg{position:absolute;left:0;top:0}
  .photo-circle{position:absolute;border-radius:50%;border:4px solid var(--paper)}
  .photo-circle--stretch{left:19px;top:390px;width:142px;height:142px;background:radial-gradient(circle at 50% 40%,#b7d77a,#4e8d2a)}
  .photo-circle--meditate{left:196px;top:336px;width:146px;height:146px;background:radial-gradient(circle at 50% 35%,#e8f2c8,#3f6e2a 75%)}
  .photo-circle--plank{left:142px;top:509px;width:148px;height:148px;background:radial-gradient(circle at 50% 45%,#9fcb5c,#3f7a22)}
  .motto{left:14px;font-family:var(--script-font);color:var(--paper);font-size:34px;white-space:nowrap}
  .motto--one{top:668px}
  .motto--two{top:702px;left:120px}
</style>
</head>
<body>

<section class="card card--info" aria-label="Flyer back: benefits and services">
  <svg class="info-bg" width="357" height="795" viewBox="0 0 357 795" aria-hidden="true">
    <rect x="0" y="0" width="357" height="350" fill="var(--leaf-pale)"/>
    <path d="M0 0H357V262C300 240 230 238 170 252C110 266 50 262 0 245Z" fill="var(--leaf)"/>
    <circle cx="4" cy="150" r="26" fill="none" stroke="var(--leaf-ring)" stroke-width="9"/>
    <circle cx="356" cy="215" r="32" fill="none" stroke="var(--leaf-ring)" stroke-width="9"/>
    <circle cx="50" cy="232" r="16" fill="var(--leaf-ring)"/>
  </svg>

  <h1 class="abs center benefits-title">Real Food is the answer to:</h1>
  <p class="benefit benefit--sun" style="left:96px;top:70px">Reverting illnesses</p>
  <p class="benefit benefit--forest" style="left:26px;top:104px">A body you love</p>
  <p class="benefit benefit--ember" style="left:179px;top:104px">Emotions in control</p>
  <p class="benefit benefit--sun" style="left:95px;top:138px">Stable blood sugar</p>
  <p class="benefit benefit--forest" style="left:24px;top:171px">Healthy digestion</p>
  <p class="benefit benefit--ember" style="left:208px;top:171px">Sound sleep</p>
  <p class="benefit benefit--sun" style="left:107px;top:205px">Blasting energy</p>

  <p class="abs center equation">REAL food<span class="plus">+</span>exercise<span class="plus">+</span>water<span class="plus">+</span>L.O.L.</p>
  <p class="abs center result"><span class="equals">=</span>“HIGH QUALITY OF LIFE “</p>

  <h2 class="abs center easy">EASY, right?</h2>
  <p class="abs center challenge"><b>Challenging:</b> certainly<br><b>Changing habits:</b> reluctance in sight!</p>
  <h2 class="abs center offer-title">WE’RE HERE TO:</h2>

  <div class="step" style="left:22px;top:530px;width:270px"><span class="step-num">1</span><span>Study YOUR unique body composition, food cravings, blockages, illnesses, and personality!</span></div>
  <div class="step" style="left:80px;top:582px;width:210px"><span class="step-num">2</span><span>Educate – guide – develop plan – and follow you up 24/7</span></div>
  <div class="step" style="left:22px;top:622px;width:230px"><span class="step-num">3</span><span>You will: taste new food, plan meals, groceries shopping.</span></div>
  <div class="step" style="left:80px;top:662px;width:210px"><span class="step-num">4</span><span>You’ll attend: meditation, cooking, and fitness classes</span></div>
  <div class="step" style="left:22px;top:703px;width:230px"><span class="step-num">5</span><span style="padding-top:6px">You’ll make new friends</span></div>

  <p class="footer footer--leaf">www.freshmeadowlifepath.net</p>
</section>

<section class="card card--cover" aria-label="Flyer front: FMLP cover">
  <div class="abs food-photo" role="img" aria-label="Photo of fresh tomatoes, yellow pepper salad and green herbs in wooden bowls"></div>

  <svg class="cover-bg" width="357" height="795" viewBox="0 0 357 795" aria-hidden="true">
    <path d="M0 375C90 350 240 345 357 368V769H0Z" fill="var(--leaf-pale)"/>
    <path d="M0 388C100 366 240 362 357 384V769H0Z" fill="var(--leaf)"/>
    <circle cx="40" cy="605" r="26" fill="var(--leaf-ring)"/>
    <circle cx="115" cy="650" r="18" fill="var(--leaf-ring)"/>
    <circle cx="320" cy="560" r="22" fill="none" stroke="var(--leaf-ring)" stroke-width="8"/>
    <circle cx="300" cy="650" r="12" fill="var(--leaf-ring)"/>
  </svg>

  <div class="abs brand"><span class="brand-dot" aria-hidden="true"></span><span class="brand-name">Freshmeadowlifepath</span></div>
  <p class="abs brand-tag">BALANCED NUTRITION, MIND, AND FITNESS</p>

  <div class="photo-circle photo-circle--stretch" role="img" aria-label="Photo of a woman stretching on grass in a park"></div>
  <div class="photo-circle photo-circle--meditate" role="img" aria-label="Photo of a woman meditating in a sunlit forest"></div>
  <div class="photo-circle photo-circle--plank" role="img" aria-label="Photo of a woman doing a plank exercise outdoors"></div>

  <p class="abs motto motto--one">Everyone deserves</p>
  <p class="abs motto motto--two">true happiness</p>

  <p class="footer footer--soft">www.freshmeadowlifepath.net</p>
</section>

</body>
</html>
```